Calloway Brewhouse Beer Can Design

Design a beer can for a boutique craft brewery located in Frankston, Victoria, AUS.
We have a focus on producing Made For Good Company beers in an ambient setting. The beer can design should be sophisticated, simple, recognizable and a little playful. The color pallet should be inviting and not too bold. The design should have identifying features that can be interchanged onto different cans for different beer types. The design must be repeatable for other beer varieties, which will each have a unique color. The can should feature black, white and purple (this should be in interchangeable color). The beer can also needs to have our Calloway Brewhouse company logo on it, this has been attached to the design brief.

Target Market(s)

The target market is aged 25+ who are social, have some disposable income and appreciate good beer, wine and food.
The beers will also be made for distribution, initially to locally to restaurants and cafés and eventually commercially.
Tourists will also be targeted due to the area the brewhouse is located (Mornington Peninsula, Victoria, AUS).

Industry/Entity Type

Hospitality

Font styles to use
Sans Serif
Script

Colors
6b449b
876aae
b7a5cd
e4daeb
000000
ffffff
959595

Requirements
Must have
• The ‘Calloway Brewhouse’ logo.
• The colour associated to this beer - purple. This should be the only colour used on the can (along with black/white/gray).
• The company tagline ‘Made For Good Company’.
• The tasting notes text ‘Bright in colour, dry on the palate and thirst quenching in the extreme, wheat and pale malts compliment each other with nuance.’
• Australian beer can requirements as per 'Requirements.png'. EPS and AI files of the requirements have been included.
Nice to have
• The logo text ‘Wendel Malt IPA’ more predominant than the Calloway Brewhouse logo.
Should not have
• Be busy, simple is best
• Beer related pictures / images
• Bold, masculine lines and fonts
• Requirements.png directly used. Please use the EPS or AI files provided.

```html
<!DOCTYPE html>
<html lang="en">
<head>
<meta charset="utf-8">
<title>Calloway Brewhouse – Wendel Malt IPA Can Label</title>
<link rel="stylesheet" href="https://fonts.googleapis.com/css2?family=Montserrat:wght@500&family=Oswald:wght@600&display=swap">
<style>
  :root {
    --backdrop: #eceeef;
    --purple-deep: #6b449b;
    --purple-mid: #876aae;
    --purple-shade: #5b3a86;
    --lilac: #e4daeb;
    --white: #ffffff;
  }
  html, body {
    margin: 0;
    width: 1200px;
    height: 1200px;
    overflow: hidden;
    background: var(--backdrop);
  }
  .canvas {
    position: relative;
    width: 1200px;
    height: 1200px;
  }
  .can-label {
    position: absolute;
    left: 380px;
    top: 110px;
    width: 440px;
    height: 920px;
    overflow: hidden;
    background: linear-gradient(90deg, var(--purple-deep) 0%, var(--purple-mid) 55%, var(--purple-deep) 100%);
  }
  .label-shapes {
    position: absolute;
    inset: 0;
  }
  .label-shapes circle { fill: var(--purple-shade); opacity: 0.75; }
  .top-strap {
    position: absolute;
    top: 12px;
    left: 0;
    width: 100%;
    margin: 0;
    text-align: center;
    font-family: "Montserrat", sans-serif;
    font-weight: 500;
    font-size: 17px;
    letter-spacing: 0.5px;
    color: var(--white);
  }
  .brand-name {
    position: absolute;
    top: 225px;
    left: 0;
    width: 100%;
    margin: 0;
    text-align: center;
    font-family: "Montserrat", sans-serif;
    font-weight: 500;
    font-size: 35px;
    line-height: 1.15;
    letter-spacing: 6px;
    color: var(--lilac);
    text-transform: uppercase;
  }
  .beer-tagline {
    position: absolute;
    top: 342px;
    left: 0;
    width: 100%;
    margin: 0;
    text-align: center;
    font-family: "Montserrat", sans-serif;
    font-weight: 500;
    font-size: 18px;
    letter-spacing: 0.5px;
    color: var(--lilac);
  }
  .beer-name {
    position: absolute;
    inset: 0;
    margin: 0;
    font-family: "Oswald", sans-serif;
    font-weight: 600;
    font-size: 112px;
    line-height: 1;
    color: var(--lilac);
    text-transform: uppercase;
  }
  .beer-name span {
    position: absolute;
    white-space: nowrap;
  }
  .beer-name .line-one { top: 445px; left: 45px; letter-spacing: -1px; }
  .beer-name .line-two { top: 570px; left: 148px; }
  .beer-name .line-three { top: 695px; left: 132px; }
</style>
</head>
<body>
  <main class="canvas">
    <section class="can-label" aria-label="Wendel Malt IPA can label">
      <svg class="label-shapes" width="440" height="920" viewBox="0 0 440 920" aria-hidden="true">
        <circle cx="140" cy="145" r="95"/>
        <circle cx="320" cy="470" r="95"/>
        <circle cx="55" cy="590" r="88"/>
        <circle cx="340" cy="790" r="100"/>
      </svg>
      <p class="top-strap">THIRST QUENCHING</p>
      <p class="brand-name">Calloway<br>Brewhouse</p>
      <p class="beer-tagline">Made for good company</p>
      <h1 class="beer-name">
        <span class="line-one">Wendel</span>
        <span class="line-two">Malt</span>
        <span class="line-three">IPA</span>
      </h1>
    </section>
  </main>
</body>
</html>
```